Hi!
We need a cool brochure / leaflet for our Flenvo product line.
These are plastic corrugated sheets which are used to make various products.
When you look at the Flenvo section on our website: http://plandexo.com/flenvo/ you will get a bit more info (the website is under construction).
We need a separate page for a few products.
But for now we need just one test page for the first product group "Surface Protection". If your design is approved as a template, we will give you the text and pics for the other products. We can set a price per page for the other pages later.
Requirements:
- Size should be A4. The leaflet will be combined into one full brochure at the end. But each page will also need to function a a separate leaflet for that particular product. (For example it will also be placed on the website as a downloadable PDF)
- Font needs to be Gill Sans MT
- This is the brand logo: https://files.quorvault.net/s/k3p81wrd/Flenvo%20logo%20-%20registered.ai
- These 3 pics should be use on leaflet: https://files.quorvault.net/sh/m72tq9xz/BBdk4wLrTn
- Here you can find the text: https://files.quorvault.net/s/v9h2ya5e/Text%20-%20Surface%20Protection.docx
- The icons in this text part (including text) also need to be placed in the brochure. The originals can be found here: https://files.quorvault.net/sh/p4n6ub0c/CCfj8sXoWe
Please think outside of the box as much as possible.
And make sure to use mainly white and the "Flenvo logo" blue.
We also have another product group which will need to be done after this project.
Looking forward to your design!
Regards,
Jorn
Construction
Plastic

```html
<!DOCTYPE html>
<html lang="en">
<head>
<meta charset="utf-8">
<title>Flenvo – Surface Protection</title>
<link href="https://fonts.googleapis.com/css2?family=Cabin:wght@400;500;600;700&display=swap" rel="stylesheet">
<style>
  :root{
    --brand-blue:#1f6ec4;
    --band-blue:#2a78c9;
    --slate:#44596b;
    --slate-dark:#3a4d5d;
    --panel:#eef1f4;
    --ink:#2b2b2b;
    --white:#ffffff;
  }
  *{box-sizing:border-box;margin:0;padding:0}
  html,body{width:857px;height:1200px;overflow:hidden;background:#fff}
  body{font-family:"Cabin",sans-serif;color:var(--ink)}
  .page{position:relative;width:857px;height:1200px;background:var(--white);overflow:hidden}

  .header-top{position:absolute;left:0;top:0;width:100%;height:23px;background:linear-gradient(#f4f7fb,#dde7f2)}
  .header-band{position:absolute;left:0;top:23px;width:100%;height:97px;background:var(--band-blue)}
  .header-rule{position:absolute;left:0;top:120px;width:100%;height:11px;background:var(--slate)}
  .header-fade{position:absolute;left:0;top:131px;width:100%;height:60px;background:linear-gradient(#e8eef5,#fff)}
  .brand-name{position:absolute;left:63px;top:40px;font-size:50px;font-weight:700;letter-spacing:4px;color:var(--white);line-height:1}
  .brand-tagline{position:absolute;left:99px;top:98px;font-size:12px;font-weight:500;color:var(--white);letter-spacing:.2px}
  .product-visual{position:absolute;left:450px;top:18px;width:310px;height:104px;
    background:linear-gradient(100deg,#f7f7f7 0 30%,#1b1b1b 30% 55%,#1c9a3c 55% 70%,#f1d91f 70% 84%,#2a78c9 84%)}

  .page-title{position:absolute;left:62px;top:153px;font-size:27px;font-weight:700;color:var(--brand-blue)}
  .intro{position:absolute;left:57px;top:200px;width:742px;font-size:13px;line-height:17.3px}
  .intro p+p{margin-top:15px}

  .tab{position:absolute;left:49px;top:332px;width:258px;height:45px;background:var(--slate);
    border-top-right-radius:18px;color:var(--white);font-size:18px;padding:12px 0 0 28px}

  .spec{position:absolute;width:175px}
  .spec-head{display:flex;align-items:center;gap:10px;height:42px}
  .spec-title{font-size:12.5px;font-weight:700;line-height:15px}
  .spec-text{margin-top:8px;font-size:11.6px;line-height:15.6px;text-align:justify}

  .ico{width:40px;height:40px;border-radius:50%;background:var(--brand-blue);flex:none;
    box-shadow:0 0 0 2px #fff,0 0 0 3px var(--brand-blue);display:flex;align-items:center;justify-content:center}
  .ico svg{width:22px;height:22px;fill:none;stroke:#fff;stroke-width:2;stroke-linecap:round;stroke-linejoin:round}

  .features-head{position:absolute;left:437px;top:417px;width:401px;height:45px;background:var(--slate);
    border-top-left-radius:16px;border-bottom-right-radius:16px;color:#fff;font-size:18px;text-align:center;padding-top:12px}
  .features{position:absolute;left:437px;top:462px;width:401px;height:325px;background:var(--panel)}
  .feature{position:absolute;width:90px;text-align:center;font-size:12px;line-height:15px}
  .feature .ico{margin:0 auto 6px}

  .options-head{position:absolute;left:437px;top:804px;width:401px;height:44px;background:var(--band-blue);
    border-top-left-radius:16px;border-bottom-right-radius:16px;color:#fff;font-size:18px;text-align:center;padding-top:11px}
  .options{position:absolute;left:437px;top:848px;width:401px;height:352px;background:var(--slate)}
  .option{position:absolute;width:170px;color:#e8edf1}
  .option .spec-head{gap:12px}
  .option .spec-title{color:#fff;font-size:13px}
  .option .ico{background:#fff;box-shadow:0 0 0 2px var(--slate),0 0 0 3px #fff}
  .option .ico svg{stroke:var(--slate)}
  .option .spec-text{font-size:11.4px;line-height:15.4px}
</style>
</head>
<body>
<div class="page">
  <div class="header-top"></div>
  <div class="header-band"></div>
  <div class="header-rule"></div>
  <div class="header-fade"></div>
  <div class="brand-name">FLENVO</div>
  <div class="brand-tagline">PLASTIC CORRUGATED SHEETS</div>
  <div class="product-visual" role="img" aria-label="Fanned stack of Flenvo sheets in white, black, green, yellow and blue"></div>

  <h1 class="page-title">Surface Protection</h1>
  <div class="intro">
    <p>Flenvo sheets are used for temporary floor and wall protection. The plastic corrugated sheets are designed to provide reusable surface protection for many fixtures and surfaces during construction. The sheets offer excellent surface protection for surfaces like concrete, tile, vinyl, wooden floors, doors, counters, and cabinets. The sheets are easy to apply and cost-effective.</p>
    <p>Flenvo sheets are similar to Plyrex sheets are also sold in by the name of PP hollow sheets, twinwall sheets, fluted boards and polypropylene corrugated sheets.</p>
  </div>

  <div class="tab">Flenvo Specifications:</div>

  <div class="spec" style="left:54px;top:410px">
    <div class="spec-head"><span class="ico"><svg viewBox="0 0 24 24"><path d="M8 3h8M12 3v16M9 19l3 3 3-3M10 8h4M10 12h4"/></svg></span><span class="spec-title">Thickness</span></div>
    <p class="spec-text">Flenvo sheets can be produced in a thickness between 1.5 and 10 mm. We can advise you on what thickness to choose depending on the purpose of use.</p>
  </div>
  <div class="spec" style="left:246px;top:410px">
    <div class="spec-head"><span class="ico"><svg viewBox="0 0 24 24"><rect x="3" y="6" width="18" height="12" rx="2"/><circle cx="14" cy="12" r="3"/><path d="M3 18v3h5"/></svg></span><span class="spec-title">Size</span></div>
    <p class="spec-text">Flenvo sheets are available in any requested size. The length can be as long as required; the width is limited to 240 cm.</p>
  </div>
  <div class="spec" style="left:54px;top:560px">
    <div class="spec-head"><span class="ico"><svg viewBox="0 0 24 24"><path d="M12 3v18M7 21h10M4 7h16M4 7l-3 7h6zM20 7l-3 7h6z"/></svg></span><span class="spec-title">Weight</span></div>
    <p class="spec-text">The weight of Flenvo sheets is expressed in GSM (grams per square meter). The higher you choose your GSM, the stronger and stiffer the material will be.</p>
  </div>
  <div class="spec" style="left:246px;top:560px">
    <div class="spec-head"><span class="ico"><svg viewBox="0 0 24 24"><path d="M4 20L12 4M4 20l4-15M4 20l8-11M4 20l11-7M4 20l15-3"/></svg></span><span class="spec-title">Color</span></div>
    <p class="spec-text">Our customers can choose any color for the sheets or artwork. Just ask us what you need, and we can provide you with a sample.</p>
  </div>
  <div class="spec" style="left:54px;top:697px">
    <div class="spec-head"><span class="ico"><svg viewBox="0 0 24 24"><path d="M9 3h6M10 3v6l-6 11h16L14 9V3M8 15h8"/></svg></span><span class="spec-title">Virgin &amp; Recycled<br>Polypropylene</span></div>
    <p class="spec-text">We can use 100% virgin polypropylene to produce your sheets. Another option is to let us recycle up to 20% of our internally regenerated polypropylene</p>
  </div>
  <div class="spec" style="left:246px;top:697px">
    <div class="spec-head"><span class="ico"><svg viewBox="0 0 24 24"><circle cx="8" cy="8" r="4"/><circle cx="16" cy="16" r="4"/><path d="M11 11l2 2"/></svg></span><span class="spec-title">Custom Printing</span></div>
    <p class="spec-text">Flenvo sheets can be supplied with high-resolution, full-color printing. Send us your design, and we can directly print it onto the sheets in our factory.</p>
  </div>
  <div class="spec" style="left:54px;top:860px">
    <div class="spec-head"><span class="ico"><svg viewBox="0 0 24 24"><path d="M12 3c1 4 6 6 6 11a6 6 0 01-12 0c0-3 2-4 3-6 0 2 1 3 2 3 0-3 1-5 1-8z"/></svg></span><span class="spec-title">Fire-Retardant<br>Sheets</span></div>
    <p class="spec-text">A fire-retardant version of Flenvo sheets is available. Please let us know the fire rating you require, and we are happy to produce them for you.</p>
  </div>
  <div class="spec" style="left:246px;top:860px">
    <div class="spec-head"><span class="ico"><svg viewBox="0 0 24 24"><rect x="3" y="11" width="18" height="9"/><path d="M7 11v9M12 11v9M17 11v9M8 4l-2 4M12 4l-2 4M16 4l-2 4"/></svg></span><span class="spec-title">Corona Treatment</span></div>
    <p class="spec-text">We give our customers the choice to print their own sheets. If you choose this option, will give the sheets a corona treatment to make sure that the sheets are well prepared for printing.</p>
  </div>
  <div class="spec" style="left:54px;top:1037px">
    <div class="spec-head"><span class="ico"><svg viewBox="0 0 24 24"><circle cx="9" cy="9" r="3"/><path d="M9 2v2M2 9h2M4 4l1.5 1.5M14 4l-1.5 1.5M4 20c2-6 8-8 16-8v8z"/></svg></span><span class="spec-title">UV Protection</span></div>
    <p class="spec-text">Flenvo sheets can be produced with a UV protectant. This can extend the lifecycle of the sheets and their print work.</p>
  </div>
  <div class="spec" style="left:246px;top:1037px">
    <div class="spec-head"><span class="ico"><svg viewBox="0 0 24 24"><circle cx="14" cy="9" r="5"/><path d="M10 13l-7 8"/></svg></span><span class="spec-title">Puncture Resistance</span></div>
    <p class="spec-text">We can supply our Flenvo sheets in any requested puncture resistance grade. Just let us know the PR you require, and we will supply the material including a test report.</p>
  </div>

  <div class="features-head">Flenvo Features:</div>
  <div class="features">
    <div class="feature" style="left:23px;top:30px"><span class="ico"><svg viewBox="0 0 24 24"><path d="M15 6c-1-1-5-2-6 0s5 3 5 6-5 3-7 1M11 3v18"/></svg></span>Cost<br>Efficient</div>
    <div class="feature" style="left:112px;top:30px"><span class="ico"><svg viewBox="0 0 24 24"><path d="M8 13V5a2 2 0 014 0v6l5 1c2 1 2 3 1 6l-1 3H9l-4-6c-1-2 1-3 3-2z"/></svg></span>Easy to<br>Install</div>
    <div class="feature" style="left:202px;top:30px"><span class="ico"><svg viewBox="0 0 24 24"><path d="M6 20c-2-5 0-12 5-15 2 0 3 2 2 4l-3 1c2 2 6 2 8 5s-1 5-4 5z"/></svg></span>Strong</div>
    <div class="feature" style="left:293px;top:30px"><span class="ico"><svg viewBox="0 0 24 24"><path d="M5 20L18 6M18 6c-9 0-13 5-11 12 7 1 11-4 11-12z"/></svg></span>Light<br>Weight</div>
    <div class="feature" style="left:23px;top:138px"><span class="ico"><svg viewBox="0 0 24 24"><path d="M3 20h18M6 20v-5h12v5M9 10l6-6M12 11l3-3"/></svg></span>Shock<br>Resistant</div>
    <div class="feature" style="left:112px;top:138px"><span class="ico"><svg viewBox="0 0 24 24"><circle cx="12" cy="12" r="8"/><path d="M12 7v5l3 2"/></svg></span>Time<br>Saving</div>
    <div class="feature" style="left:202px;top:138px"><span class="ico"><svg viewBox="0 0 24 24"><path d="M3 12a9 9 0 0118 0zM12 12v7a2 2 0 01-4 0"/></svg></span>Waterproof</div>
    <div class="feature" style="left:293px;top:138px"><span class="ico"><svg viewBox="0 0 24 24"><path d="M6 19c-2-2-2-6 2-9l5-4 5 5-4 5c-3 4-6 5-8 3zM15 3l1 2M19 6l2 1"/></svg></span>Washable</div>
    <div class="feature" style="left:23px;top:236px"><span class="ico"><svg viewBox="0 0 24 24"><path d="M4 21h16M8 21l8-14M14 4l5 3M7 15l4 2"/></svg></span>Chemical<br>Resistant</div>
    <div class="feature" style="left:112px;top:236px"><span class="ico"><svg viewBox="0 0 24 24"><rect x="4" y="7" width="16" height="13" rx="2"/><path d="M9 7V4h6v3M12 10v7M8.5 13.5h7"/></svg></span>Hygienic<br>(antibacterial)</div>
    <div class="feature" style="left:202px;top:236px"><span class="ico"><svg viewBox="0 0 24 24"><circle cx="12" cy="12" r="9"/><path d="M6 6l12 12M10 9h4v7h-4zM8 11h2M14 11h2M8 14h2M14 14h2"/></svg></span>Bug<br>Resistant</div>
  </div>

  <div class="options-head">Veltacor Options:</div>
  <div class="options">
    <div class="option" style="left:21px;top:30px">
      <div class="spec-head"><span class="ico"><svg viewBox="0 0 24 24"><rect x="3" y="6" width="18" height="12" rx="2"/><circle cx="14" cy="12" r="3"/><path d="M3 18v3h5"/></svg></span><span class="spec-title">Specific Sizes</span></div>
      <p class="spec-text">We know that some projects and production lines require special sizes. That's why it is possible to order Veltacor products in different sizes and thicknesses.</p>
    </div>
    <div class="option" style="left:219px;top:26px">
      <div class="spec-head"><span class="ico"><svg viewBox="0 0 24 24"><circle cx="8" cy="8" r="4"/><circle cx="16" cy="16" r="4"/><path d="M11 11l2 2"/></svg></span><span class="spec-title">Logo Printing</span></div>
      <p class="spec-text">It's possible to order Veltacor products with a custom-made print. Company logos printed on Veltacor products can be great for marketing purposes and branding.</p>
    </div>
    <div class="option" style="left:21px;top:177px">
      <div class="spec-head"><span class="ico"><svg viewBox="0 0 24 24"><path d="M12 3c1 4 6 6 6 11a6 6 0 01-12 0c0-3 2-4 3-6 0 2 1 3 2 3 0-3 1-5 1-8z"/></svg></span><span class="spec-title">Fire-Retardant</span></div>
      <p class="spec-text">Some Veltacor products can be produced with fire-resistant additives. Veltacor fire-rated products prevent flammability of surfaces in areas that are fire-sensitive.</p>
    </div>
  </div>
</div>
</body>
</html>
```